Business Card for new Architectural Firm

I intend to practice in a rural mountain community in upstate NY, focusing on residential and light commercial projects, including second home / vacation properties. I wish to convey a feeling of rural outdoorsy modernity.

Color is important - bold and urbane. Secondary or tertiary colors preferred.

Font is important, idiosyncratic is ok

Optionally, I may choose to use the name Brackenfold Studio. If used as part of your design, all of the Must Haves are still required.

Images uploaded are logos I like

Industry/Entity Type

Residential

Contact Information for Business Card

Lionel Harwicke
Architect (This word should stand alone or be associated with my name - not license number)
NY License No. 052816
lionel@designlhq.com
607 382 9154

Font styles to use
Sans Serif
Decorative

Requirements
Must have
• Whatever files I need to best utilize your design
• PDF
• JPG
• EPS
• Vectorwhatsit
Nice to have
• Logo or element that can be incorporated into other print material.
• Could be a font based card
Should not have
• no clip art
• No templates
• no floor plans
• no building photographs

```html
<!DOCTYPE html>
<html lang="en">
<head>
<meta charset="utf-8">
<title>Lionel Harwicke — Architect Business Card</title>
<link href="https://fonts.googleapis.com/css2?family=Roboto:wght@300;400&display=swap" rel="stylesheet">
<style>
  :root {
    --backdrop: #2b2b2b;
    --card: #f4f4f4;
    --card-shade: #e6e6e6;
    --name-blue: #4a7fc8;
    --leaf-green: #62b246;
    --band-text: #ffffff;
  }
  * { margin: 0; padding: 0; box-sizing: border-box; }
  html, body {
    width: 1200px;
    height: 900px;
    overflow: hidden;
    background: var(--backdrop);
    font-family: "Roboto", Arial, sans-serif;
  }
  .business-card {
    position: absolute;
    left: 150px;
    top: 193px;
    width: 900px;
    height: 514px;
    background: radial-gradient(ellipse at 50% 35%, #ffffff 0%, var(--card) 55%, var(--card-shade) 100%);
    display: flex;
    flex-direction: column;
  }
  .identity {
    flex: 1;
    display: flex;
    flex-direction: column;
    align-items: center;
  }
  .identity-dot {
    margin-top: 112px;
    width: 118px;
    height: 118px;
    border-radius: 50%;
    background: var(--leaf-green);
  }
  .identity-name {
    margin-top: 42px;
    font-weight: 400;
    font-size: 40px;
    letter-spacing: 1.5px;
    color: var(--name-blue);
    line-height: 1;
  }
  .identity-title {
    margin-top: 6px;
    font-weight: 300;
    font-size: 18px;
    letter-spacing: 26px;
    padding-left: 26px;
    color: var(--leaf-green);
    line-height: 1;
  }
  .contact-band {
    height: 96px;
    background: var(--leaf-green);
    color: var(--band-text);
    font-weight: 300;
    font-size: 20px;
    letter-spacing: 1px;
    display: flex;
    flex-direction: column;
    align-items: center;
    justify-content: center;
    gap: 6px;
  }
  .contact-line {
    display: flex;
    align-items: center;
    gap: 10px;
  }
  .contact-icon { width: 18px; height: 14px; fill: var(--band-text); }
  .contact-divider { padding: 0 4px; }
</style>
</head>
<body>
  <div class="business-card">
    <div class="identity">
      <div class="identity-dot"></div>
      <div class="identity-name">Lionel Harwicke</div>
      <div class="identity-title">ARCHITECT</div>
    </div>
    <div class="contact-band">
      <div class="contact-line">
        <svg class="contact-icon" viewBox="0 0 18 14" aria-hidden="true">
          <path d="M1 4 C4 0 14 0 17 4 L14 6 L12 4 L6 4 L4 6 Z"/>
          <path d="M4 7 L14 7 L16 13 L2 13 Z"/>
        </svg>
        <span class="contact-phone">607 382 9154</span>
        <span class="contact-divider">|</span>
        <svg class="contact-icon" viewBox="0 0 18 14" aria-hidden="true">
          <path d="M1 2 L17 2 L17 12 L1 12 Z M2 3 L9 8 L16 3 Z" fill-rule="evenodd"/>
        </svg>
        <span class="contact-email">lionel@designlhq.com</span>
      </div>
      <div class="contact-line">
        <span class="contact-license">NY License No. 052816</span>
      </div>
    </div>
  </div>
</body>
</html>
```